*** Business Card Design Project

As a starting point, please take a look at our website www.plentarohire.com as a starting point.

We are looking for you to design our new business cards for plentarohire, something funky, cool and potentially unusual/different.

Good luck.

Industry/Entity Type

Business

```html
<!DOCTYPE html>
<html lang="en">
<head>
<meta charset="utf-8">
<title>plentarohire – Business Card</title>
<link rel="stylesheet" href="https://fonts.googleapis.com/css2?family=Josefin+Sans:wght@400&family=Open+Sans:wght@600;700&display=swap">
<style>
  :root {
    --stage: #dfe3e6;
    --paper: #ffffff;
    --brand-orange: #f08a24;
    --ink: #2b2b2b;
    --ink-soft: #444444;
    --shadow: rgba(0, 0, 0, 0.18);
  }
  * { box-sizing: border-box; margin: 0; padding: 0; }
  html, body {
    width: 1200px;
    height: 960px;
    overflow: hidden;
  }
  body {
    background: var(--stage);
    position: relative;
    font-family: "Josefin Sans", sans-serif;
    color: var(--ink);
  }
  .card {
    position: absolute;
    top: 325px;
    width: 540px;
    height: 310px;
    box-shadow: 0 6px 18px var(--shadow);
    overflow: hidden;
  }
  .card--front { left: 45px; background: var(--paper); }
  .card--back  { left: 615px; background: var(--brand-orange); }

  .brand-name {
    font-family: "Open Sans", sans-serif;
    font-weight: 700;
    color: var(--ink);
    letter-spacing: 0.5px;
  }
  .brand-tagline {
    font-family: "Open Sans", sans-serif;
    font-weight: 600;
    color: var(--ink);
    letter-spacing: 1.2px;
  }

  /* Front */
  .card--front .brand { position: absolute; left: 30px; top: 26px; }
  .card--front .brand-name { font-size: 36px; line-height: 1; }
  .card--front .brand-tagline { font-size: 14px; margin-top: 6px; }

  .accent-band {
    position: absolute;
    left: 232px;
    right: 0;
    top: 112px;
    height: 46px;
    background: var(--brand-orange);
  }
  .person { position: absolute; left: 30px; top: 128px; }
  .person-name { font-size: 26px; }
  .person-role { font-size: 20px; margin-top: 10px; }

  .contact-list {
    position: absolute;
    left: 30px;
    bottom: 26px;
    list-style: none;
    font-size: 16px;
    line-height: 22px;
  }
  .contact-list li, .office li { display: flex; align-items: center; gap: 8px; }
  .contact-icon { width: 12px; height: 12px; flex: none; fill: var(--brand-orange); }

  .office {
    position: absolute;
    left: 356px;
    top: 196px;
    list-style: none;
    font-size: 13px;
    line-height: 18px;
    color: var(--ink-soft);
  }
  .office .contact-icon { width: 9px; height: 9px; }
  .office .indent { padding-left: 17px; }

  /* Back */
  .card--back .brand {
    position: absolute;
    left: 0; right: 0;
    top: 112px;
    text-align: center;
  }
  .card--back .brand-name { font-size: 40px; line-height: 1; }
  .card--back .brand-tagline { font-size: 16px; margin-top: 8px; }
</style>
</head>
<body>

  <section class="card card--front" aria-label="Business card front">
    <div class="brand">
      <div class="brand-name">plentarohire</div>
      <div class="brand-tagline">Executive Search</div>
    </div>

    <div class="accent-band"></div>

    <div class="person">
      <div class="person-name">Martin Calloway</div>
      <div class="person-role">Managing Director</div>
    </div>

    <ul class="contact-list">
      <li>
        <svg class="contact-icon" viewBox="0 0 12 12" aria-hidden="true"><path d="M2.5 1 L4.5 1 L5 3.5 L3.8 4.5 Q5 7 7.5 8.2 L8.5 7 L11 7.5 L11 9.5 Q10.5 11 9 11 Q1 10 1 3 Q1 1.5 2.5 1 Z"/></svg>
        <span>(+44) 0203 555 0142</span>
      </li>
      <li>
        <svg class="contact-icon" viewBox="0 0 12 12" aria-hidden="true"><rect x="3" y="0.5" width="6" height="11" rx="1"/><rect x="4" y="2" width="4" height="5" fill="#fff"/></svg>
        <span>(+44) 07700 900461</span>
      </li>
      <li>
        <svg class="contact-icon" viewBox="0 0 12 12" aria-hidden="true"><rect x="0.5" y="2.5" width="11" height="7"/><path d="M0.5 2.5 L6 6.5 L11.5 2.5" fill="none" stroke="#fff" stroke-width="1"/></svg>
        <span>martin@plentarohire.com</span>
      </li>
      <li>
        <svg class="contact-icon" viewBox="0 0 12 12" aria-hidden="true"><circle cx="6" cy="6" r="5.5"/></svg>
        <span>martincplentarohire</span>
      </li>
    </ul>

    <ul class="office">
      <li>
        <svg class="contact-icon" viewBox="0 0 12 12" aria-hidden="true"><rect x="0.5" y="2.5" width="11" height="7"/><path d="M0.5 2.5 L6 6.5 L11.5 2.5" fill="none" stroke="#fff" stroke-width="1"/></svg>
        <span>info@plentarohire.com</span>
      </li>
      <li>
        <svg class="contact-icon" viewBox="0 0 12 12" aria-hidden="true"><circle cx="6" cy="6" r="5.5"/><path d="M0.5 6 H11.5 M6 0.5 V11.5" stroke="#fff" stroke-width="1"/></svg>
        <span>www.plentarohire.com</span>
      </li>
      <li class="indent">14 - 16 Harlow Row</li>
      <li class="indent">London EC2X 4JD</li>
    </ul>
  </section>

  <section class="card card--back" aria-label="Business card back">
    <div class="brand">
      <div class="brand-name">plentarohire</div>
      <div class="brand-tagline">Executive Search</div>
    </div>
  </section>

</body>
</html>
```